Wedding DJ Services Flyer

Need to make a classy flyer showing and describing different services we offer. I have actual photos from weddings we have done in the past. Stock photos are ok too. Just looking for a front and back, blank space for pricing. Need website and other company info (logo) on the flyer. Front needs to pop with a tagline that screams wedding dj and as soon as a customer sees it, they want to book us. Services we offer are DJ/Emcee, Karaoke, Uplighting, Custom Monogram Projection, Dancing on the Clouds, Custom Love Story Video Slideshow (see my photos, stock photos are ok too).Dominic Hale Sound Collective, We have been in business since 1998 and provide DJ Event services to all of central and northeastern Pennsylvania. want social media icons on flyer (facebook,instagram,twitter) by website (www.Dhsc.org) and email (Dominic@dhsc.org), phone number 555-318-2264 (call or Text)MORE PHOTOS AVAIL BY REQUEST. Designer should have some knowledge or prior design with this type of business

Target Market(s)

brides and grooms 18-50 yoa

Industry/Entity Type

Entertainment Industry

Colors

Designer to choose colors to be used in the design.

Requirements
Must have
• Photos and descriptions of services we offer

```html
<!DOCTYPE html>
<html lang="en">
<head>
<meta charset="utf-8">
<title>Wedding DJ Flyer – Dominic Hale Sound Collective</title>
<link href="https://fonts.googleapis.com/css2?family=Oswald:wght@500;600;700&family=Montserrat:wght@400;500;700;800&display=swap" rel="stylesheet">
<style>
:root{
  --purple:#6a1fa0;
  --violet:#8a2bb8;
  --pink:#e0185f;
  --magenta:#c21a7e;
  --ink:#1d1d24;
  --text:#3a3a44;
  --paper:#ffffff;
  --panel:#f1f0f4;
  --stage:#e4e4e6;
  --brand-grad:linear-gradient(135deg,var(--pink),var(--purple));
}
*{box-sizing:border-box;margin:0;padding:0}
html,body{width:1200px;height:800px;overflow:hidden}
body{background:var(--stage);font-family:'Montserrat',sans-serif;position:relative}

.flyer{position:absolute;top:40px;width:500px;height:720px;background:var(--paper);overflow:hidden;box-shadow:0 6px 18px rgba(0,0,0,.18)}
.flyer--back{left:70px}
.flyer--front{left:630px}

.photo{position:absolute;display:block}
.wave{position:absolute;left:0;width:100%;display:block}

/* shared footer */
.footer{position:absolute;left:0;bottom:0;width:100%;height:120px}
.footer__info{position:absolute;left:20px;top:40px;color:#fff;width:170px}
.footer__label{font-size:9.5px;font-weight:800;letter-spacing:.3px}
.footer__phone{font-size:19px;font-weight:800;margin:1px 0 4px}
.footer__note{font-size:8px;line-height:1.3}
.footer__contact{position:absolute;left:210px;top:56px;color:#fff;font-size:8.5px;line-height:1.9}
.footer__contact div{display:flex;align-items:center;gap:6px}
.footer__contact svg{width:11px;height:11px}
.social{position:absolute;right:20px;top:60px;display:flex;gap:8px}
.social span{width:22px;height:22px;border-radius:50%;background:#fff;display:block}

/* back */
.back-hero{left:0;top:0;width:100%;height:330px;background:linear-gradient(135deg,#5a1a78 0%,#8e2c8e 55%,#b13a86 100%)}
.brand-bubble{position:absolute;left:290px;top:-70px;width:240px;height:240px;border-radius:50%;background:#fff;display:flex;align-items:center;justify-content:center;padding:60px 60px 0 20px}
.brand-bubble p{font-family:'Oswald',sans-serif;font-weight:600;color:var(--ink);font-size:24px;line-height:1.15;text-align:center}
.tagline-circle{position:absolute;left:18px;top:180px;width:170px;height:170px;border-radius:50%;background:var(--brand-grad);border:6px solid rgba(255,255,255,.85);display:flex;align-items:center;justify-content:center;text-align:center;color:#fff;font-weight:800;font-size:17px;line-height:1.3}
.gallery-circle{border-radius:50%;border:5px solid #fff;background:linear-gradient(135deg,#3b1a6e,#7b3fc0)}
.gallery-circle--a{left:-25px;top:340px;width:170px;height:170px}
.gallery-circle--b{left:125px;top:320px;width:100px;height:100px}
.gallery-circle--c{left:90px;top:420px;width:130px;height:130px}
.prices{position:absolute;left:258px;top:325px;width:230px;height:240px;background:var(--panel);border-radius:10px;padding:18px 20px}
.prices h2{font-size:15px;font-weight:800;color:var(--ink);margin-bottom:12px}
.price-row{display:flex;align-items:center;gap:12px;margin-bottom:7px}
.price-row strong{color:var(--pink);font-size:13px;font-weight:800;width:48px}
.price-row span{font-size:8px;font-weight:700;color:var(--ink);line-height:1.2}

/* front */
.front-hero{left:0;top:0;width:100%;height:330px;background:linear-gradient(120deg,#4b1c8c 0%,#8a2bb8 45%,#d02a7a 100%)}
.front-couple{left:270px;top:0;width:230px;height:310px;background:linear-gradient(160deg,#c0326e,#7a1e6a)}
.front-dj{left:110px;top:110px;width:200px;height:200px;background:linear-gradient(180deg,#8a8a94,#2b2b33)}
.headline{position:absolute;left:28px;top:30px;font-family:'Oswald',sans-serif;font-weight:700;color:#fff;line-height:1}
.headline__main{font-size:62px;display:block}
.headline__sub{font-size:42px;display:block;margin-top:12px}
.brand-seal{position:absolute;left:335px;top:220px;width:160px;height:160px;border-radius:50%;background:var(--brand-grad);border:6px solid #fff;display:flex;flex-direction:column;align-items:center;justify-content:center;color:#fff;font-family:'Oswald',sans-serif;font-weight:600;text-align:center;line-height:1.05}
.brand-seal p{font-size:22px}
.intro{position:absolute;left:20px;top:340px;width:225px}
.intro h2{font-size:15px;font-weight:800;color:var(--ink);line-height:1.15}
.intro h2 em{font-style:normal;color:var(--pink);display:block}
.intro p{font-size:9.5px;line-height:1.45;color:var(--text);margin-top:8px;text-align:justify}
.front-venue{left:20px;top:462px;width:225px;height:120px;background:linear-gradient(135deg,#2a1150,#6b2cb0 60%,#a04fd0)}
.services{position:absolute;left:262px;top:392px;width:230px}
.services h2{font-size:15px;font-weight:800;color:var(--ink);margin-bottom:10px}
.services ul{list-style:none}
.services li{display:flex;gap:8px;font-size:11.5px;color:var(--text);line-height:1.2;margin-bottom:7px}
.services li svg{flex:none;width:14px;height:14px;margin-top:1px}
</style>
</head>
<body>

<section class="flyer flyer--back" aria-label="Flyer back">
  <div class="photo back-hero" role="img" aria-label="Bride and groom sharing a first dance in a reception hall"></div>
  <div class="brand-bubble"><p>Dominic Hale<br>Sound Collective</p></div>
  <div class="tagline-circle">LET US<br>ENTERTAIN<br>YOUR NEXT<br>EVENT</div>
  <svg class="wave" style="top:290px;height:300px" viewBox="0 0 500 300" preserveAspectRatio="none" aria-hidden="true">
    <path d="M0 50 C120 0 300 0 500 40 L500 300 L0 300 Z" fill="#fff"/>
  </svg>
  <div class="photo gallery-circle gallery-circle--a" role="img" aria-label="Couple dancing on the clouds effect"></div>
  <div class="photo gallery-circle gallery-circle--b" role="img" aria-label="Uplit reception hall with set tables"></div>
  <div class="photo gallery-circle gallery-circle--c" role="img" aria-label="Guests dancing under purple lights"></div>
  <div class="prices">
    <h2>OUR PRICES</h2>
    <div class="price-row"><strong>1.400$</strong><span>LOREM IPSUM<br>SIT DOLOR</span></div>
    <div class="price-row"><strong>1.400$</strong><span>LOREM IPSUM<br>SIT DOLOR</span></div>
    <div class="price-row"><strong>1.400$</strong><span>LOREM IPSUM<br>SIT DOLOR</span></div>
    <div class="price-row"><strong>1.400$</strong><span>LOREM IPSUM<br>SIT DOLOR</span></div>
    <div class="price-row"><strong>1.400$</strong><span>LOREM IPSUM<br>SIT DOLOR</span></div>
    <div class="price-row"><strong>1.400$</strong><span>LOREM IPSUM<br>SIT DOLOR</span></div>
    <div class="price-row"><strong>1.400$</strong><span>LOREM IPSUM<br>SIT DOLOR</span></div>
  </div>
  <div class="footer">
    <svg class="wave" style="top:0;height:120px" viewBox="0 0 500 120" preserveAspectRatio="none" aria-hidden="true">
      <defs><linearGradient id="footB" x1="0" x2="1"><stop offset="0" stop-color="#e0185f"/><stop offset=".5" stop-color="#c21a7e"/><stop offset="1" stop-color="#6a1fa0"/></linearGradient></defs>
      <path d="M0 25 C150 0 330 45 500 15 L500 120 L0 120 Z" fill="url(#footB)"/>
    </svg>
    <div class="footer__info">
      <div class="footer__label">FOR MORE INFO</div>
      <div class="footer__phone">555-318-2264</div>
      <div class="footer__note">We Provide DJ Event services to all of central and northeastern Pennsylvania</div>
    </div>
    <div class="footer__contact">
      <div><svg viewBox="0 0 12 12"><circle cx="6" cy="6" r="5" fill="none" stroke="#fff" stroke-width="1.2"/><path d="M1 6h10M6 1c2 2.5 2 7.5 0 10M6 1c-2 2.5-2 7.5 0 10" fill="none" stroke="#fff" stroke-width="1"/></svg>www.Dhsc.org</div>
      <div><svg viewBox="0 0 12 12"><rect x="1" y="2.5" width="10" height="7" fill="#fff"/><path d="M1 2.5l5 4 5-4" fill="none" stroke="#c21a7e" stroke-width="1"/></svg>Dominic@dhsc.org</div>
    </div>
    <div class="social"><span></span><span></span></div>
  </div>
</section>

<section class="flyer flyer--front" aria-label="Flyer front">
  <div class="photo front-hero" role="img" aria-label="Purple and pink wedding reception backdrop"></div>
  <div class="photo front-couple" role="img" aria-label="Bride and groom embracing under warm lights"></div>
  <div class="photo front-dj" role="img" aria-label="DJ in a suit mixing on turntables"></div>
  <h1 class="headline"><span class="headline__main">WEDDING</span><span class="headline__sub">DJ</span></h1>
  <svg class="wave" style="top:295px;height:60px" viewBox="0 0 500 60" preserveAspectRatio="none" aria-hidden="true">
    <path d="M0 20 C140 0 330 40 500 10 L500 60 L0 60 Z" fill="#fff"/>
  </svg>
  <div class="brand-seal"><p>DOMINIC HALE</p><p>SOUND</p><p>COLLECTIVE</p></div>
  <div class="intro">
    <h2>LET US ENTERTAIN <em>YOUR NEXT EVENT!</em></h2>
    <p>Established in 1998, we have been serving the Hazleton area and all of Northeast Pennsylvania for over 20 years. We offer Event DJ Services, Emcee, Karaoke, and Smartphone Trivia.</p>
  </div>
  <div class="photo front-venue" role="img" aria-label="Reception hall with purple uplighting"></div>
  <div class="services">
    <h2>OUR SERVICES</h2>
    <ul>
      <li><svg viewBox="0 0 14 14"><circle cx="7" cy="7" r="7" fill="#c21a7e"/><path d="M3.8 7.2l2.2 2.2 4.2-4.4" fill="none" stroke="#fff" stroke-width="1.6"/></svg>DJ/Emcee</li>
      <li><svg viewBox="0 0 14 14"><circle cx="7" cy="7" r="7" fill="#c21a7e"/><path d="M3.8 7.2l2.2 2.2 4.2-4.4" fill="none" stroke="#fff" stroke-width="1.6"/></svg>Karaoke</li>
      <li><svg viewBox="0 0 14 14"><circle cx="7" cy="7" r="7" fill="#c21a7e"/><path d="M3.8 7.2l2.2 2.2 4.2-4.4" fill="none" stroke="#fff" stroke-width="1.6"/></svg>Uplighting</li>
      <li><svg viewBox="0 0 14 14"><circle cx="7" cy="7" r="7" fill="#c21a7e"/><path d="M3.8 7.2l2.2 2.2 4.2-4.4" fill="none" stroke="#fff" stroke-width="1.6"/></svg>Custom Monogram<br>Projection</li>
      <li><svg viewBox="0 0 14 14"><circle cx="7" cy="7" r="7" fill="#c21a7e"/><path d="M3.8 7.2l2.2 2.2 4.2-4.4" fill="none" stroke="#fff" stroke-width="1.6"/></svg>Dancing on the<br>Clouds</li>
      <li><svg viewBox="0 0 14 14"><circle cx="7" cy="7" r="7" fill="#c21a7e"/><path d="M3.8 7.2l2.2 2.2 4.2-4.4" fill="none" stroke="#fff" stroke-width="1.6"/></svg>Custom Love Story<br>Video Slideshow</li>
    </ul>
  </div>
  <div class="footer">
    <svg class="wave" style="top:0;height:120px" viewBox="0 0 500 120" preserveAspectRatio="none" aria-hidden="true">
      <defs><linearGradient id="footF" x1="0" x2="1"><stop offset="0" stop-color="#e0185f"/><stop offset=".5" stop-color="#c21a7e"/><stop offset="1" stop-color="#6a1fa0"/></linearGradient></defs>
      <path d="M0 25 C150 0 330 45 500 15 L500 120 L0 120 Z" fill="url(#footF)"/>
    </svg>
    <div class="footer__info">
      <div class="footer__label">FOR MORE INFO</div>
      <div class="footer__phone">555-318-2264</div>
      <div class="footer__note">We Provide DJ Event services to all of central and northeastern Pennsylvania</div>
    </div>
    <div class="footer__contact">
      <div><svg viewBox="0 0 12 12"><circle cx="6" cy="6" r="5" fill="none" stroke="#fff" stroke-width="1.2"/><path d="M1 6h10M6 1c2 2.5 2 7.5 0 10M6 1c-2 2.5-2 7.5 0 10" fill="none" stroke="#fff" stroke-width="1"/></svg>www.Dhsc.org</div>
      <div><svg viewBox="0 0 12 12"><rect x="1" y="2.5" width="10" height="7" fill="#fff"/><path d="M1 2.5l5 4 5-4" fill="none" stroke="#c21a7e" stroke-width="1"/></svg>Dominic@dhsc.org</div>
    </div>
    <div class="social"><span></span><span></span><span></span></div>
  </div>
</section>

</body>
</html>
```